10-slide template for ESG report for small businesses in Europe

Presentation goal: for owners of small businesses in Europe to report on their ESG metrics to various internal and external stakeholders, but typically used as part of their annual (financial) report.
Who is the target audience: small business owners/managers in Europe (these are business people, but not very corporate)
How is it going to be used: this template will be used to generate PDF reports automatically based on various inputs. The final output will not be reviewed or corrected by a human; hence we need to make sure that the template is flexible enough to be used for a variety of different inputs (specifically, in some cases there will be no input, and in some cases there will be many characters).
Desired look and feel: following VelloCrest brand style guide (attached). It's for business use so it's somewhat formal, but I do not want it to come across too corporate, so it's OK if there are playful elements.
What is the catch: the fact the template will need to be flexible enough to allow for the report to still look OK even if a certain fields do not have a value (specifically, as mentioned earlier there are some text fields that are likely going to be empty, but could have up to 1000 characters of text).
Illustrations: to keep it generic and relevant for a variety of businesses across all of Europe it's probably better to use simple flat style illustrations instead of photos. I've been using https://brimstudiofy.com/ to create those (see example attached) but I'm open to anything.
Lastly: please note that I'm very open to changing the position and size of all copy, tables, illustrations etc. I know I'm a terrible designer - that's why I'm here ;-)
Look and feel
Each slider illustrates characteristics of the customer's brand and the style your logo design should communicate.

```html
<!DOCTYPE html>
<html lang="en">
<head>
<meta charset="utf-8">
<title>ESG Report – Advisory Statement</title>
<link rel="stylesheet" href="https://fonts.googleapis.com/css2?family=Arimo:wght@400;700&display=swap">
<style>
  :root {
    --navy: #0f1f56;
    --white: #ffffff;
    --placeholder: #4d8dff;
    --muted: #b4bccb;
    --lime: #94c11f;
    --button-face: #ececec;
    --button-edge: #8a8a8a;
    --ink: #111111;
  }
  * { margin: 0; padding: 0; box-sizing: border-box; }
  html, body {
    width: 1200px;
    height: 679px;
    overflow: hidden;
    background: var(--navy);
  }
  .slide {
    position: relative;
    width: 1200px;
    height: 679px;
    background: var(--navy);
    font-family: "Arimo", Arial, sans-serif;
    color: var(--white);
  }
  .brand {
    position: absolute;
    left: 136px;
    top: 64px;
    display: flex;
    align-items: center;
    gap: 14px;
  }
  .brand-square {
    width: 44px;
    height: 44px;
    background: var(--white);
  }
  .brand-name {
    font-size: 50px;
    font-weight: 700;
    letter-spacing: -0.5px;
    color: var(--white);
    line-height: 1;
  }
  .decor-square {
    position: absolute;
    left: 899px;
    top: 59px;
    width: 221px;
    height: 221px;
    background: var(--lime);
  }
  .placeholder {
    color: var(--placeholder);
    font-weight: 700;
  }
  .date {
    position: absolute;
    left: 137px;
    top: 169px;
    font-size: 12px;
  }
  .statement {
    position: absolute;
    left: 137px;
    top: 216px;
    width: 566px;
    font-size: 12px;
    line-height: 17.6px;
  }
  .statement p + p { margin-top: 17.6px; }
  .gap { display: inline-block; width: 70px; }
  .signature-field {
    position: absolute;
    left: 138px;
    top: 464px;
    width: 151px;
    height: 31px;
    background: var(--button-face);
    border: 1px solid var(--button-edge);
    border-radius: 3px;
    color: var(--ink);
    font-size: 22px;
    text-align: center;
    line-height: 29px;
  }
  .signatory {
    position: absolute;
    left: 137px;
    top: 537px;
    font-size: 12px;
    line-height: 18px;
  }
  .footer {
    position: absolute;
    left: 143px;
    top: 644px;
    font-size: 12px;
    color: var(--muted);
  }
</style>
</head>
<body>
  <main class="slide">
    <div class="brand">
      <span class="brand-square"></span>
      <span class="brand-name">VelloCrest</span>
    </div>

    <div class="decor-square"></div>

    <p class="date placeholder">[date]</p>

    <section class="statement">
      <p>As an independent advisory, VelloCrest provided guidance in the preparation of this ESG report for <span class="placeholder">[business name]</span><span class="gap"></span>.</p>
      <p>The company applied the recommendations of major reporting frameworks, adhered to best practices in ESG reporting and defined appropriate data collection procedures, all in line with VelloCrest's recommended approach. While no specific details were verified, the overall assessment confirms the process reflects a genuine commitment to comprehensive, thoughtful, and transparent disclosure across key sustainability focus areas.</p>
      <p>The report aims to deliver balanced, transparent representations of policies, programs, metrics, and results related to environmental, social, and governance topics. We view this as a valuable resource for stakeholders and encourage continuous progress towards ambitious, science-based sustainability goals guided by inclusiveness, accountability, and innovation.</p>
    </section>

    <div class="signature-field">signature</div>

    <div class="signatory">
      <p>J.R. Maren, LLM</p>
      <p>VelloCrest</p>
    </div>

    <footer class="footer">
      <span class="placeholder">[reporting period]</span> Environmental, Social, and Governance Report | <span class="placeholder">[business name]</span>
    </footer>
  </main>
</body>
</html>
```